SEO AND WEB DESIGN COMPANY BUSINESS CARD DESIGN

I need an eye catching , simple business card design that will match my logo . I need 2 versions of it ( white background and black background) - SOME PEOPLE DID NOT GET IT AND SENDING US FRONT WHITE BACK WHITE VERSIONS WHICH IS NOT CORRECT.

ONE VERSION SHOULD BE BACK AND FRONT ALL BLACK , SECOND VERSION SHOULD BE BACK AND FRONT ALL WHITE

logo psd files are attached for both versions. The business card is going to have : First Name- Last name - position - phone numbers

```html
<!DOCTYPE html>
<html lang="en">
<head>
<meta charset="utf-8">
<title>Brightpath Studio – Business Card</title>
<link href="https://fonts.googleapis.com/css2?family=Oswald:wght@600&family=Ubuntu:wght@500&family=Roboto:wght@400&display=swap" rel="stylesheet">
<style>
  :root {
    --backdrop: #2e2e30;
    --card: #1b1b1d;
    --white: #f4f4f4;
    --blue: #1a9be0;
    --steel: #5b6470;
    --muted: #8a8d92;
  }
  * { margin: 0; padding: 0; box-sizing: border-box; }
  html, body { width: 799px; height: 1200px; overflow: hidden; }
  body {
    background: var(--backdrop);
    display: flex;
    flex-direction: column;
    align-items: center;
    justify-content: center;
    gap: 110px;
    font-family: "Roboto", sans-serif;
  }
  .card {
    position: relative;
    width: 620px;
    height: 354px;
    background: var(--card);
    border-radius: 4px;
    overflow: hidden;
    box-shadow: 0 10px 30px rgba(0,0,0,0.45);
  }
  .brand {
    display: flex;
    align-items: center;
    gap: 12px;
  }
  .brand-dot {
    width: 18px; height: 18px;
    border-radius: 50%;
    background: var(--blue);
    flex: none;
  }
  .brand-name {
    font-family: "Oswald", sans-serif;
    font-weight: 600;
    color: var(--white);
    text-transform: uppercase;
    letter-spacing: 1px;
    line-height: 1;
    white-space: nowrap;
  }

  /* Front */
  .card-front .brand {
    position: absolute;
    top: 120px; left: 0; right: 0;
    justify-content: center;
  }
  .card-front .brand-name { font-size: 52px; }
  .front-web {
    position: absolute;
    left: 0; right: 0; top: 262px;
    display: flex; justify-content: center; align-items: center; gap: 14px;
    color: var(--white);
    font-size: 17px;
  }
  .front-web .dash { width: 44px; height: 3px; background: var(--blue); }
  .front-band { position: absolute; left: 0; bottom: 0; width: 620px; height: 30px; }

  /* Back */
  .card-back .brand {
    position: absolute;
    top: 160px; left: 34px;
    gap: 10px;
  }
  .card-back .brand-dot { width: 14px; height: 14px; }
  .card-back .brand-name { font-size: 26px; }
  .divider {
    position: absolute;
    left: 318px; top: 60px;
    width: 1px; height: 234px;
    background: var(--muted);
  }
  .contact {
    position: absolute;
    left: 346px; top: 78px;
    color: var(--white);
  }
  .contact-name {
    font-family: "Ubuntu", sans-serif;
    font-weight: 500;
    font-size: 24px;
    color: var(--blue);
  }
  .contact-role { font-size: 15px; margin-top: 2px; margin-bottom: 20px; }
  .contact-line {
    display: flex; align-items: center; gap: 12px;
    font-size: 15px; margin-bottom: 6px;
  }
  .contact-icon {
    width: 14px; height: 14px; flex: none;
    display: block;
  }
  .contact-address { font-size: 15px; line-height: 1.35; margin-top: 6px; }
</style>
</head>
<body>

  <section class="card card-front" aria-label="Card front">
    <div class="brand">
      <span class="brand-dot"></span>
      <span class="brand-name">Brightpath Studio</span>
    </div>
    <div class="front-web">
      <span class="dash"></span>
      <span>www.brightpathstudio.com</span>
      <span class="dash"></span>
    </div>
    <svg class="front-band" viewBox="0 0 620 30" aria-hidden="true">
      <defs>
        <linearGradient id="bandFade" x1="0" x2="1">
          <stop offset="0" stop-color="#5b6470"/>
          <stop offset="0.35" stop-color="#1a9be0"/>
          <stop offset="1" stop-color="#1a9be0"/>
        </linearGradient>
      </defs>
      <rect x="0" y="18" width="620" height="12" fill="url(#bandFade)"/>
    </svg>
  </section>

  <section class="card card-back" aria-label="Card back">
    <div class="brand">
      <span class="brand-dot"></span>
      <span class="brand-name">Brightpath Studio</span>
    </div>
    <div class="divider"></div>
    <div class="contact">
      <div class="contact-name">Dana Lee Carter</div>
      <div class="contact-role">Managing Director</div>
      <div class="contact-line">
        <svg class="contact-icon" viewBox="0 0 16 16" aria-hidden="true"><path fill="#1a9be0" d="M3 1h3l1.5 4-2 1.3a9 9 0 0 0 4.2 4.2L11 8.5l4 1.5v3a2 2 0 0 1-2 2A12 12 0 0 1 1 3a2 2 0 0 1 2-2z"/></svg>
        <span>555-010-2244</span>
      </div>
      <div class="contact-line">
        <svg class="contact-icon" viewBox="0 0 16 16" aria-hidden="true"><path d="M1 3h14v10H1z M1 3l7 6 7-6" fill="none" stroke="#1a9be0" stroke-width="1.6"/></svg>
        <span>dana@yourwebsite.com</span>
      </div>
      <div class="contact-line">
        <svg class="contact-icon" viewBox="0 0 16 16" aria-hidden="true"><circle cx="8" cy="8" r="6.5" fill="none" stroke="#1a9be0" stroke-width="1.4"/><path d="M1.5 8h13M8 1.5c-3 3.5-3 9.5 0 13M8 1.5c3 3.5 3 9.5 0 13" fill="none" stroke="#1a9be0" stroke-width="1.2"/></svg>
        <span>www.yourwebsite.com</span>
      </div>
      <div class="contact-address">234 Anywhere St., Any City,<br>Any Town, US 123456</div>
    </div>
  </section>

</body>
</html>
```